Save the Date for 77th birthday fundraiser

We need a design for a Save the Date as we are preparing to celebrate our founder Dale Penwarden’s 77 birthday next year.
We would like a professional illustrated Save the Date with the theme “How it started, How it’s going”. Attached is a picture from the early 70’s and another one from yesterday. We want him to look his absolute best.
We need the date, location, and contact details to RSVP incorporated into the design:
April 9
Milford Avery House, Austin Texas
team@guidebrightpath.com
AND PLEASE REMEMBER THIS IS A SURPRISE!
We would also like to include elements that evoke what he does: Author (he’s published 2 books), Speaker (a microphone), Business Coach, and Entrepreneur.
Feelings we would like to evoke when people see the image: Would like people to think we are a professional company that is throwing a fun event for all the clients and friends Dale has made along his extraordinary 50-year career.
Thank you so much!

```html
<!DOCTYPE html>
<html lang="en">
<head>
<meta charset="utf-8">
<title>Save the Date – Dale Penwarden</title>
<link rel="stylesheet" href="https://fonts.googleapis.com/css2?family=Poppins:wght@300;400;500;600;700;800&family=Yellowtail&display=swap">
<style>
  :root {
    --backdrop: #c9d2da;
    --paper: #f4f4f2;
    --navy: #2b2c66;
    --navy-deep: #1c1d4d;
    --teal: #3fb3b5;
    --teal-dark: #2a8f9c;
    --white: #ffffff;
    --sepia-light: #e6e1d8;
    --sepia-dark: #5b544c;
  }
  * { box-sizing: border-box; margin: 0; padding: 0; }
  html, body {
    width: 994px; height: 1200px; overflow: hidden;
    background: var(--backdrop);
    font-family: "Poppins", sans-serif;
  }
  .card {
    position: absolute; left: 97px; top: 40px;
    width: 800px; height: 1119px;
    background: var(--paper);
    overflow: hidden;
    color: var(--navy);
  }
  .heading { position: absolute; left: 0; width: 100%; text-align: center; }
  .celebrating { top: 68px; font-size: 28px; font-weight: 700; letter-spacing: 0.32em; padding-left: 0.32em; }
  .years { top: 118px; font-size: 23px; font-weight: 300; letter-spacing: 0.3em; padding-left: 0.3em; }
  .honoree { top: 148px; font-family: "Yellowtail", cursive; font-size: 74px; font-weight: 400; line-height: 1.1; }
  .tagline { top: 232px; font-size: 18px; font-weight: 600; letter-spacing: 0.34em; padding-left: 0.34em; }

  .wave { position: absolute; left: 0; top: 0; width: 800px; height: 1119px; }

  .art { position: absolute; border-radius: 28px; }
  .art-icons {
    left: 42px; top: 369px; width: 710px; height: 300px;
    background: linear-gradient(135deg, var(--teal) 0%, var(--teal-dark) 50%, var(--navy) 100%);
    opacity: 0.85;
  }
  .art-then {
    left: 27px; top: 369px; width: 290px; height: 450px;
    background: linear-gradient(180deg, var(--sepia-dark) 0%, var(--sepia-light) 55%, #8a8177 100%);
    border: 5px solid var(--white);
  }
  .art-now {
    left: 263px; top: 288px; width: 320px; height: 590px;
    background: linear-gradient(180deg, #3e3832 0%, #d9d4cc 35%, #4a443e 70%, #2e2a26 100%);
    border: 5px solid var(--white);
  }

  .badge {
    position: absolute; left: 136px; top: 750px; width: 255px; height: 235px;
    background: linear-gradient(160deg, var(--navy) 0%, var(--navy-deep) 100%);
    border: 4px solid #8fd0d2; border-radius: 16px;
    transform: rotate(-4deg);
    box-shadow: 0 14px 24px rgba(20, 20, 60, 0.45);
    text-align: center; line-height: 1;
  }
  .badge-save { display: block; margin-top: 26px; font-size: 62px; font-weight: 800; color: var(--teal); }
  .badge-the { display: block; margin-top: -6px; font-size: 40px; font-weight: 300; font-style: italic; color: var(--white); }
  .badge-date { display: block; margin-top: -8px; font-size: 70px; font-weight: 800; color: var(--teal); }
  .badge-day { display: block; margin-top: 2px; font-size: 24px; font-weight: 500; color: var(--white); }

  .rsvp { position: absolute; left: 463px; top: 938px; color: #e4e6f2; }
  .rsvp-label { font-size: 19px; font-weight: 300; letter-spacing: 0.22em; margin-bottom: 6px; }
  .rsvp-venue { font-size: 19px; font-weight: 500; line-height: 1.55; }
  .rsvp-email { font-size: 16px; font-weight: 400; margin-top: 6px; }
</style>
</head>
<body>
  <main class="card">
    <div class="art art-icons" role="img" aria-label="Illustrated icons of a fountain pen nib, a microphone and a presentation screen with a rising chart"></div>
    <div class="art art-then" role="img" aria-label="Early 1970s photo of Dale in a top hat and waistcoat"></div>
    <div class="art art-now" role="img" aria-label="Recent photo of Dale in a top hat, white shirt and dark vest"></div>

    <svg class="wave" viewBox="0 0 800 1119" aria-hidden="true">
      <path d="M0 758 C 200 890, 600 880, 800 535" fill="none" stroke="var(--teal)" stroke-width="14"/>
      <path d="M0 772 C 200 904, 600 894, 800 552 L800 1119 L0 1119 Z" fill="var(--navy)"/>
    </svg>

    <h2 class="heading celebrating">CELEBRATING</h2>
    <p class="heading years">EXTRAORDINARY 50 YEARS OF</p>
    <h1 class="heading honoree">Dale Penwarden</h1>
    <p class="heading tagline">GUIDE TO THE BRIGHT PATH</p>

    <div class="badge">
      <span class="badge-save">Save</span>
      <span class="badge-the">the</span>
      <span class="badge-date">Date</span>
      <span class="badge-day">April 9, 2022</span>
    </div>

    <div class="rsvp">
      <p class="rsvp-label">RSVP:</p>
      <p class="rsvp-venue">Milford Avery House,<br>Austin Texas</p>
      <p class="rsvp-email">team@guidebrightpath.com</p>
    </div>
  </main>
</body>
</html>
```